Sandwich Board Poster

1. Copy this design with different text provided below & replace 4 black & white photo's with attached
2. Copy this design with different text provided below & remove photo's

Replacement Text:

Every Friday night 7:00pm-8:30pm
Kelowen Stretch & Movement Hall
627 Corliss Rd Wenmoor

Free Kirtan Experience
Torven Alidu & Company

Dimensions of media: 24 x 36

CHANGE IN TEXT TO READ " JOIN US TONIGHT 7:00PM-8:30PM " ( NOT FRIDAY NIGHT)

Duplicate the Kirtan Experience poster with replacement text.

```html
<!DOCTYPE html>
<html lang="en">
<head>
<meta charset="utf-8">
<title>Kirtan Experience Poster</title>
<link rel="stylesheet" href="https://fonts.googleapis.com/css2?family=Cinzel:wght@700;900&family=Open+Sans:wght@700;800&display=swap">
<style>
  :root {
    --backdrop: #eceeef;
    --band-rust: rgba(160, 74, 32, 0.92);
    --band-umber: rgba(74, 38, 20, 0.9);
    --band-cocoa: rgba(62, 32, 18, 0.94);
    --band-cream: rgba(246, 240, 232, 0.9);
    --band-copper: rgba(170, 82, 36, 0.92);
    --frame-gold: #a8905a;
    --frame-white: #ffffff;
    --ink-light: #ffffff;
    --ink-dark: #4a1f10;
  }
  * { margin: 0; padding: 0; box-sizing: border-box; }
  html, body {
    width: 1000px;
    height: 1200px;
    overflow: hidden;
    background: var(--backdrop);
  }
  .poster {
    position: absolute;
    left: 105px;
    top: 27px;
    width: 790px;
    height: 1146px;
    display: block;
    box-shadow: 0 2px 10px rgba(0,0,0,0.18);
  }
  .title {
    font-family: "Cinzel", Georgia, serif;
    font-weight: 900;
    fill: var(--ink-light);
  }
  .title--kirtan { font-size: 90px; }
  .title--experience { font-size: 58px; }
  .details {
    font-family: "Open Sans", Arial, sans-serif;
    font-weight: 800;
    font-size: 23px;
    fill: var(--ink-light);
  }
  .feature {
    font-family: "Open Sans", Arial, sans-serif;
    font-weight: 800;
    fill: var(--ink-dark);
  }
  .feature--headline { font-size: 27px; }
  .feature--host { font-size: 21px; }
  .invite {
    font-family: "Open Sans", Arial, sans-serif;
    font-weight: 700;
    font-size: 17px;
    fill: var(--ink-light);
  }
  .photo-frame { fill: var(--frame-white); }
  .center-frame { fill: var(--frame-gold); }
</style>
</head>
<body>
<svg class="poster" viewBox="0 0 665 965" xmlns="http://www.w3.org/2000/svg">
  <defs>
    <clipPath id="poster-bounds"><rect width="665" height="965"/></clipPath>
    <radialGradient id="tile-tone" cx="50%" cy="50%" r="70%">
      <stop offset="0%" stop-color="#b48a5e"/>
      <stop offset="60%" stop-color="#c4a177"/>
      <stop offset="100%" stop-color="#a88058"/>
    </radialGradient>
    <linearGradient id="musician-tone" x1="0" y1="0" x2="1" y2="1">
      <stop offset="0%" stop-color="#d8d2c8"/>
      <stop offset="100%" stop-color="#4a3f3a"/>
    </linearGradient>
    <linearGradient id="sunset-tone" x1="0" y1="0" x2="1" y2="1">
      <stop offset="0%" stop-color="#e6a23c"/>
      <stop offset="100%" stop-color="#3a3550"/>
    </linearGradient>
    <linearGradient id="saint-tone" x1="0" y1="0" x2="0" y2="1">
      <stop offset="0%" stop-color="#e48a3a"/>
      <stop offset="100%" stop-color="#e9c24a"/>
    </linearGradient>
    <linearGradient id="dance-tone" x1="0" y1="0" x2="1" y2="1">
      <stop offset="0%" stop-color="#c98a6a"/>
      <stop offset="100%" stop-color="#6a2a20"/>
    </linearGradient>
  </defs>

  <g clip-path="url(#poster-bounds)">
    <rect class="tile-field" width="665" height="965" fill="url(#tile-tone)" role="img" aria-label="Ornamental tiled pattern with scrolling floral motifs in tan and brown"/>

    <!-- diagonal bands -->
    <polygon class="band band--subtitle" points="140,0 330,0 665,335 665,525" fill="var(--band-umber)"/>
    <polygon class="band band--title" points="0,330 330,0 500,0 0,500" fill="var(--band-rust)"/>
    <polygon class="band band--feature" points="665,445 665,595 300,965 145,965" fill="var(--band-cream)"/>
    <polygon class="band band--invite" points="665,595 665,755 455,965 300,965" fill="var(--band-copper)"/>
    <polygon class="band band--schedule" points="0,487 0,701 260,965 478,965" fill="var(--band-cocoa)"/>

    <!-- headline -->
    <text class="title title--kirtan" text-anchor="middle" dominant-baseline="central" textLength="375" lengthAdjust="spacingAndGlyphs" transform="translate(160 273) rotate(-45)">KIRTAN</text>
    <text class="title title--experience" text-anchor="middle" dominant-baseline="central" textLength="430" lengthAdjust="spacingAndGlyphs" transform="translate(460 233) rotate(45)">EXPERIENCE</text>

    <!-- center feature image -->
    <g transform="translate(330 488) rotate(45)">
      <rect class="center-frame" x="-99" y="-99" width="198" height="198"/>
      <rect x="-81" y="-81" width="162" height="162" fill="#c09d72"/>
      <rect class="photo-frame" x="-74" y="-74" width="148" height="148"/>
      <rect x="-70" y="-70" width="140" height="140" fill="url(#saint-tone)" role="img" aria-label="Painting of a devotional figure in saffron robes with a flower garland"/>
    </g>

    <!-- small photos -->
    <g transform="translate(355 263) rotate(45)">
      <rect class="photo-frame" x="-58" y="-58" width="116" height="116"/>
      <rect x="-54" y="-54" width="108" height="108" fill="url(#sunset-tone)" role="img" aria-label="Photo of a musician playing harmonium before a golden moon"/>
    </g>
    <g transform="translate(100 493) rotate(45)">
      <rect class="photo-frame" x="-58" y="-58" width="116" height="116"/>
      <rect x="-54" y="-54" width="108" height="108" fill="url(#musician-tone)" role="img" aria-label="Photo of a guitarist singing into a microphone"/>
    </g>
    <g transform="translate(545 463) rotate(45)">
      <rect class="photo-frame" x="-58" y="-58" width="116" height="116"/>
      <rect x="-54" y="-54" width="108" height="108" fill="url(#sunset-tone)" role="img" aria-label="Photo of two musicians playing instruments in warm light"/>
    </g>
    <g transform="translate(295 688) rotate(45)">
      <rect class="photo-frame" x="-58" y="-58" width="116" height="116"/>
      <rect x="-54" y="-54" width="108" height="108" fill="url(#dance-tone)" role="img" aria-label="Photo of dancers with raised arms"/>
    </g>

    <!-- schedule -->
    <g class="schedule" transform="translate(197 733) rotate(45)">
      <text class="details" text-anchor="middle" dominant-baseline="central" y="0">JOIN US TONIGHT 7:00PM-8:30PM</text>
      <text class="details" text-anchor="middle" dominant-baseline="central" y="35">Kelowen Stretch &amp; Movement Hall</text>
      <text class="details" text-anchor="middle" dominant-baseline="central" y="69">627 Corliss Rd Wenmoor</text>
    </g>

    <!-- feature -->
    <g class="feature-block" transform="translate(478 687) rotate(-45)">
      <text class="feature feature--headline" text-anchor="middle" dominant-baseline="central" y="0">Free Kirtan Experience</text>
      <text class="feature feature--host" text-anchor="middle" dominant-baseline="central" y="24">Torven Alidu &amp; Company</text>
    </g>

    <!-- invitation -->
    <g class="invite-block" transform="translate(490 803) rotate(-45)">
      <text class="invite" text-anchor="middle" dominant-baseline="central" y="0">come, rest and relax</text>
      <text class="invite" text-anchor="middle" dominant-baseline="central" y="24">with kirtan meditation</text>
    </g>
  </g>
</svg>
</body>
</html>
```